Publishing company needs book cover for multi-author book

Copperfield Lane Publishing needs a book cover designed for a multi-author book called Harbor Lanterns: Unlikely Triumph Accounts from Remarkable Pioneers. We would like to see designs that incorporates the design theme of the image attached and possibly the image itself. The book will be used by the contributing authors who are  are Healers, Psychics, Coaches, Energy Workers, Astrologers, Numerologist, Tarot Card Readers and will be using this book to both market their business and use in their practices.  The final design should communicate  these spiritual practices.
I would love to see
1. A silhouette or image of a woman holding a ball or circle with the attached art inside of.
2. The concepts in the attached art brought into a  new design or  enhancing the original art.

Target Market(s)
The clients and audiences of the contributing authors
Industry/Entity Type
Spiritual, Body Mind Spirit, Evolving Continuousness, Alternative Healing
Colors
Designer to choose colors to be used in the design.
Requirements
Must have
- Title- Harbor Lanterns: Unlikely Triumph Accounts from Remarkable Pioneers. and the name of the publishing company: Copperfield Lane Publishing

Nice to have
- I would love to have the concept of the artwork coming to life through an image of woman, visionary, healer who is healing the world through her modalities.

Should not have
- Dimensions - 6X9

```html
<!DOCTYPE html>
<html lang="en">
<head>
<meta charset="utf-8">
<title>Harbor Lanterns – Book Cover Spread</title>
<link rel="stylesheet" href="https://fonts.googleapis.com/css2?family=Poiret+One&family=Source+Sans+3:wght@700&display=swap">
<style>
  :root {
    --page: #ffffff;
    --back-cover: #231f1c;
    --spine: #2a2624;
    --spine-edge: #4a4541;
    --front-bg: #0b0a0a;
    --smoke: #3a3634;
    --title: #e8562a;
    --subtitle: #f0901e;
    --rule: #3d3936;
    --publisher: #c06a6a;
    --orb-light: #f4e6dc;
    --orb-warm: #d9734f;
    --orb-violet: #a892c4;
  }
  * { margin: 0; padding: 0; box-sizing: border-box; }
  html, body {
    width: 1200px; height: 849px; overflow: hidden;
    background: var(--page);
  }
  .spread {
    position: relative; width: 1200px; height: 849px;
  }
  .back-cover {
    position: absolute; left: 142px; top: 97px;
    width: 427px; height: 642px;
    background: var(--back-cover);
  }
  .spine {
    position: absolute; left: 569px; top: 97px;
    width: 19px; height: 642px;
    background: var(--spine);
    border-left: 1px solid var(--spine-edge);
  }
  .spine-title {
    position: absolute; left: 50%; top: 144px;
    transform: translateX(-50%);
    writing-mode: vertical-rl;
    font-family: "Poiret One", sans-serif;
    font-size: 10.5px; white-space: nowrap;
    color: var(--subtitle);
  }
  .spine-title .lead { color: var(--title); }
  .front-cover {
    position: absolute; left: 588px; top: 97px;
    width: 429px; height: 642px;
    background:
      radial-gradient(ellipse 60% 40% at 30% 25%, rgba(70,66,63,.55), transparent 70%),
      radial-gradient(ellipse 55% 35% at 80% 60%, rgba(60,56,53,.5), transparent 70%),
      var(--front-bg);
    overflow: hidden;
  }
  .cover-title {
    position: absolute; left: 0; right: 0; top: 40px;
    text-align: center;
    font-family: "Poiret One", sans-serif;
  }
  .cover-title .main {
    display: block; font-size: 36px; line-height: 1; color: var(--title);
    padding-left: 30px;
  }
  .cover-title .rule {
    display: block; width: 230px; height: 1px; margin: 12px auto 8px;
    background: var(--rule);
  }
  .cover-title .sub {
    display: block; font-size: 25px; line-height: 34px; color: var(--subtitle);
  }
  .cover-art {
    position: absolute; left: 0; top: 160px; width: 429px; height: 405px;
    background:
      radial-gradient(circle at 53% 45%, var(--orb-light) 0, #e7c8b8 22%, var(--orb-warm) 34%, #9a8f8a 44%, rgba(210,200,195,.35) 47%, transparent 52%),
      radial-gradient(circle at 40% 40%, rgba(168,146,196,.45), transparent 40%),
      linear-gradient(to bottom, transparent 70%, #141212 100%);
  }
  .publisher {
    position: absolute; left: 0; right: 0; top: 585px;
    text-align: center;
    font-family: "Source Sans 3", sans-serif; font-weight: 700;
    font-size: 18px; letter-spacing: .3px;
    color: var(--publisher);
  }
</style>
</head>
<body>
<div class="spread">
  <div class="back-cover"></div>
  <div class="spine">
    <span class="spine-title"><span class="lead">Harbor Lanterns:</span> Unlikely Triumph Accounts from Remarkable Pioneers</span>
  </div>
  <div class="front-cover">
    <h1 class="cover-title">
      <span class="main">Harbor Lanterns:</span>
      <span class="rule"></span>
      <span class="sub">Unlikely Triumph Accounts</span>
      <span class="sub">from Remarkable Pioneers</span>
    </h1>
    <div class="cover-art" role="img" aria-label="Illustration of a glowing moon orb with painted moon phases and swirling colours, a meditating woman in silhouette seated on reflective water under a starry sky"></div>
    <p class="publisher">Copperfield Lane Publishing</p>
  </div>
</div>
</body>
</html>
```